Thank you for shopping with us business card

We would like a thank you card for our rebranded business. We used to be "Brindle Goods" but are now "Marlow Finds. Old thank you card and new logo will be attached for reference. New thank you card does not have to be same design as old thank you card, but please use new logo.
Shopmart URL is now marlowfinds.shopmart.example
Instagram is @Marlow_Finds
Email is marlowfinds@mailbox.example
Thank you!

Contact Information for Business Card

Shopmart site, email, Instagram

```html
<!DOCTYPE html>
<html lang="en">
<head>
<meta charset="utf-8">
<title>Marlow Finds – Thank You Card</title>
<link rel="stylesheet" href="https://fonts.googleapis.com/css2?family=Kaushan+Script&family=Montserrat:wght@400;500;600&display=swap">
<style>
  :root {
    --backdrop: #4b5053;
    --paper: #f4f4f4;
    --ink: #141414;
    --silver: #b9b9b9;
    --white: #ffffff;
  }
  * { margin: 0; padding: 0; box-sizing: border-box; }
  html, body { width: 1200px; height: 824px; overflow: hidden; }
  body {
    background: var(--backdrop);
    font-family: "Montserrat", sans-serif;
    color: var(--ink);
    display: flex;
    align-items: center;
    justify-content: center;
    gap: 40px;
  }
  .card {
    position: relative;
    width: 540px;
    height: 309px;
    background: var(--paper);
    overflow: hidden;
    box-shadow: 0 18px 40px rgba(0,0,0,0.35);
  }
  /* Front */
  .brand { position: absolute; left: 120px; top: 70px; display: flex; align-items: center; }
  .brand-square { width: 62px; height: 62px; background: var(--ink); }
  .brand-divider { width: 1.5px; height: 96px; background: var(--ink); margin: 0 22px 0 26px; }
  .brand-name {
    font-weight: 600; font-size: 27px; line-height: 1.1;
    text-transform: uppercase; letter-spacing: 0.5px;
  }
  .contacts { position: absolute; left: 120px; top: 200px; list-style: none; }
  .contact { display: flex; align-items: center; gap: 10px; font-size: 13px; font-weight: 500; margin-bottom: 10px; }
  .contact-icon { width: 20px; height: 20px; flex: none; }
  /* Back */
  .wave { position: absolute; inset: 0; }
  .thanks-heading {
    position: absolute; left: 34px; top: 42px;
    font-family: "Kaushan Script", cursive;
    font-weight: 400; font-size: 60px; line-height: 1;
    color: var(--ink);
  }
  .thanks-sub {
    position: absolute; left: 92px; top: 138px;
    font-size: 11px; font-weight: 500; text-transform: uppercase; letter-spacing: 1px;
  }
  .back-brand {
    position: absolute; right: 28px; top: 26px;
    display: flex; align-items: center; gap: 8px;
    font-size: 13px; font-weight: 600;
  }
  .back-brand-square { width: 22px; height: 22px; background: var(--ink); }
  .message {
    position: absolute; left: 140px; right: 20px; top: 222px;
    color: var(--white); text-align: center;
    font-size: 13.5px; font-weight: 500; text-transform: uppercase;
    letter-spacing: 1.2px; line-height: 1.75;
  }
</style>
</head>
<body>

  <section class="card card-front">
    <div class="brand">
      <span class="brand-square"></span>
      <span class="brand-divider"></span>
      <h1 class="brand-name">Marlow<br>Finds</h1>
    </div>
    <ul class="contacts">
      <li class="contact">
        <svg class="contact-icon" viewBox="0 0 20 20" aria-hidden="true">
          <circle cx="10" cy="10" r="10" fill="#141414"/>
          <g fill="none" stroke="#fff" stroke-width="1">
            <circle cx="10" cy="10" r="5.5"/>
            <ellipse cx="10" cy="10" rx="2.4" ry="5.5"/>
            <line x1="4.5" y1="10" x2="15.5" y2="10"/>
          </g>
        </svg>
        marlowfinds.shopmart.example
      </li>
      <li class="contact">
        <svg class="contact-icon" viewBox="0 0 20 20" aria-hidden="true">
          <circle cx="10" cy="10" r="10" fill="#141414"/>
          <rect x="5" y="6.5" width="10" height="7" fill="none" stroke="#fff" stroke-width="1"/>
          <polyline points="5,6.5 10,10.5 15,6.5" fill="none" stroke="#fff" stroke-width="1"/>
        </svg>
        marlowfinds@mailbox.example
      </li>
      <li class="contact">
        <svg class="contact-icon" viewBox="0 0 20 20" aria-hidden="true">
          <circle cx="10" cy="10" r="10" fill="#141414"/>
        </svg>
        @Marlow_Finds
      </li>
    </ul>
  </section>

  <section class="card card-back">
    <svg class="wave" viewBox="0 0 540 309" aria-hidden="true">
      <path d="M0,223 C120,223 200,198 280,158 S440,98 540,103 L540,309 L0,309 Z" fill="#141414"/>
      <path d="M0,213 C120,213 200,188 280,148 S440,88 540,93" fill="none" stroke="var(--silver)" stroke-width="4"/>
    </svg>
    <h2 class="thanks-heading">Thank you</h2>
    <p class="thanks-sub">For your purchase</p>
    <div class="back-brand"><span class="back-brand-square"></span>Marlow Finds</div>
    <p class="message">
      Your purchase made my day and I hope<br>
      this package brightens yours.<br>
      Please come back and leave a review!
    </p>
  </section>

</body>
</html>
```